Local electrical company needs two flyers designed

We are a small local electrical contracting company and are in desperate need of a awasome flyer design to help grow our business
Updates

hi everyone.

please keep the logo off the front page.
it can go on the rear.

We are really trying to portray a angry/frustrated women BECAUSE her lights are broken.
not light globes

Target Market(s)

Home owners

Industry/Entity Type

Electrical

Font styles to use
Serif

Requirements

```html
<!DOCTYPE html>
<html lang="en">
<head>
<meta charset="utf-8">
<title>Bright Spark Electrical – LED Downlights Flyer</title>
<link rel="stylesheet" href="https://fonts.googleapis.com/css2?family=Arimo:wght@400;700&family=Oswald:wght@500;600&family=Roboto+Condensed:ital,wght@0,400;0,700;1,700&display=swap">
<style>
  :root {
    --page-bg: #e8e5e0;
    --front-dark: #07080c;
    --yellow: #f7e718;
    --white: #ffffff;
    --orange: #f27c1f;
    --blue-text: #1b72b8;
    --green: #2fa84a;
    --bubble-blue: #1c9ce0;
    --ink: #222222;
  }
  * { box-sizing: border-box; margin: 0; padding: 0; }
  html, body { width: 849px; height: 1200px; overflow: hidden; }
  body { background: var(--page-bg); position: relative; font-family: "Arimo", Arial, sans-serif; }

  .flyer { position: absolute; left: 112px; width: 612px; height: 409px; overflow: hidden; }

  /* Front */
  .flyer-front {
    top: 128px;
    background:
      radial-gradient(ellipse 260px 190px at 460px 30px, rgba(60,100,190,.55), transparent 70%),
      radial-gradient(ellipse 220px 170px at 570px 70px, rgba(40,80,170,.5), transparent 70%),
      var(--front-dark);
  }
  .front-headline {
    position: absolute; left: 38px; top: 43px;
    color: var(--yellow); font-weight: 700; font-size: 36px; line-height: 40px; letter-spacing: 1px;
  }
  .front-subline {
    position: absolute; left: 38px; top: 187px;
    color: var(--white); font-weight: 700; font-size: 21px; line-height: 25px; letter-spacing: .5px;
  }
  .front-tagline {
    position: absolute; left: 37px; top: 300px;
    color: var(--white); font-weight: 400; font-size: 40px; line-height: 48px; letter-spacing: 1.6px;
  }
  .front-tagline .accent { color: var(--yellow); }
  .burning-note {
    position: absolute; left: 262px; top: 128px; width: 350px; height: 216px;
    border-radius: 10px 0 0 10px;
    background: linear-gradient(180deg, rgba(242,132,36,.9) 0%, rgba(214,160,70,.85) 30%, #8fcf86 55%, #5aa766 100%);
  }

  /* Back */
  .flyer-back { top: 670px; background: var(--white); }
  .call-box {
    position: absolute; left: 16px; top: 2px; width: 392px; height: 80px;
    background: var(--orange); border-radius: 0 14px 14px 14px; padding: 4px 0 0 16px;
  }
  .call-box .phone { font-family: "Oswald", sans-serif; font-weight: 600; font-size: 30px; line-height: 38px; color: var(--yellow); }
  .call-box .more, .call-box .link { font-family: "Roboto Condensed", sans-serif; color: var(--white); font-size: 15px; line-height: 17px; }
  .call-box .link { font-weight: 700; font-size: 15.5px; }

  .intro {
    position: absolute; left: 26px; top: 94px;
    font-family: "Roboto Condensed", sans-serif; font-weight: 700; font-size: 15.5px; line-height: 18px; color: var(--blue-text);
  }
  .save-badge {
    position: absolute; left: 23px; top: 140px; width: 148px; height: 52px;
    background: var(--green); clip-path: polygon(0 0, 88% 0, 100% 50%, 88% 100%, 0 100%);
    font-family: "Oswald", sans-serif; font-weight: 600; color: var(--yellow); font-size: 36px; line-height: 52px; padding-left: 10px;
  }
  .save-badge sup { font-size: 18px; vertical-align: 14px; }
  .save-detail {
    position: absolute; left: 180px; top: 141px;
    font-family: "Roboto Condensed", sans-serif; font-weight: 700; font-size: 23px; line-height: 25px; color: var(--green); letter-spacing: .6px;
  }
  .benefits { position: absolute; left: 22px; top: 206px; list-style: none; }
  .benefits li {
    position: relative; padding-left: 22px; margin-bottom: 4px;
    font-family: "Roboto Condensed", sans-serif; font-weight: 700; font-size: 13px; line-height: 17px; color: var(--blue-text);
  }
  .benefits svg { position: absolute; left: 0; top: 2px; }
  .payment-cards { position: absolute; left: 52px; top: 320px; display: flex; gap: 8px; }
  .payment-cards span { width: 46px; height: 28px; border-radius: 3px; background: #c9d3df; box-shadow: 0 1px 2px rgba(0,0,0,.3); }

  .review {
    position: absolute; left: 265px; top: 202px; width: 337px; height: 142px;
    background: var(--bubble-blue); border-radius: 16px; padding: 11px 12px 0 18px;
    font-family: "Roboto Condensed", sans-serif; font-style: italic; font-weight: 700; font-size: 14.5px; line-height: 20px; color: var(--white);
  }
  .review .author { text-align: right; display: block; padding-right: 2px; }
  .review-tail { position: absolute; left: 520px; top: 340px; }

  .mascot {
    position: absolute; left: 478px; top: 14px; width: 125px; height: 116px; border-radius: 10px;
    background: linear-gradient(160deg, #bfe2f7 0%, #8fbf63 45%, #c4392c 100%);
  }
  .brand-name {
    position: absolute; left: 442px; top: 132px; width: 140px;
    font-family: "Roboto Condensed", sans-serif; font-weight: 700; font-size: 16px; line-height: 18px; color: var(--orange);
  }

  .web {
    position: absolute; left: 20px; top: 355px;
    font-family: "Arimo", sans-serif; font-size: 21px; color: var(--orange);
  }
  .web b { font-weight: 700; }
  .fine-print {
    position: absolute; left: 14px; top: 384px; display: flex; gap: 6px;
    font-family: "Arimo", sans-serif; font-size: 10.5px; color: var(--ink);
  }
  .fine-print .divider { border-left: 1.5px solid var(--ink); padding-left: 5px; }
</style>
</head>
<body>

<section class="flyer flyer-front">
  <h1 class="front-headline">TIRED OF<br>REPLACING<br>BULBS?</h1>
  <p class="front-subline">LIGHTS KEEP<br>FLICKING OFF?</p>
  <div class="burning-note" role="img" aria-label="A hundred dollar banknote on fire beneath two downlights"></div>
  <p class="front-tagline"><span class="accent">BURNING</span> A<br>HOLE IN YOUR <span class="accent">WALLET?</span></p>
</section>

<section class="flyer flyer-back">
  <div class="call-box">
    <p class="phone">CALL NOW : 1300 555 018</p>
    <p class="more">For more information visit</p>
    <p class="link">www.brightsparkelectrical.com.au/leddownlights</p>
  </div>

  <div class="mascot" role="img" aria-label="Superhero electrician mascot holding up a light bulb"></div>
  <p class="brand-name">BRIGHT SPARK<br>ELECTRICAL</p>

  <p class="intro">Replace your old $$$ burning halogen downlights<br>with new money saving led downlights</p>

  <div class="save-badge">SAVE <sup>$</sup>25</div>
  <p class="save-detail">OFF EVERY 3RD<br>DOWNLIGHT REPLACED</p>

  <ul class="benefits">
    <li><svg width="14" height="14" viewBox="0 0 14 14"><circle cx="7" cy="7" r="7" fill="#f5a21c"/><path d="M3.5 7.2l2.3 2.3 4.6-4.8" stroke="#fff" stroke-width="1.8" fill="none"/></svg>SPECIALISING IN DOMESTIC<br>ELECTRICAL REPAIRS</li>
    <li><svg width="14" height="14" viewBox="0 0 14 14"><circle cx="7" cy="7" r="7" fill="#f5a21c"/><path d="M3.5 7.2l2.3 2.3 4.6-4.8" stroke="#fff" stroke-width="1.8" fill="none"/></svg>ON TIME GUARANTEE OR $100 OFF</li>
    <li><svg width="14" height="14" viewBox="0 0 14 14"><circle cx="7" cy="7" r="7" fill="#f5a21c"/><path d="M3.5 7.2l2.3 2.3 4.6-4.8" stroke="#fff" stroke-width="1.8" fill="none"/></svg>UP FRONT PRICING</li>
    <li><svg width="14" height="14" viewBox="0 0 14 14"><circle cx="7" cy="7" r="7" fill="#f5a21c"/><path d="M3.5 7.2l2.3 2.3 4.6-4.8" stroke="#fff" stroke-width="1.8" fill="none"/></svg>NO MESS GUARANTEED</li>
  </ul>

  <div class="payment-cards" aria-label="Accepted payment cards"><span></span><span></span><span></span></div>

  <blockquote class="review">
    Excellent electrician! Turns up on time, friendly<br>and a can-do attitude. Did several jobs here<br>including installing (and recommending) LED<br>lights in our kitchen and dining room. No mess,<br>quick and efficient. Highly recommended
    <span class="author">R.Tollard Ashfield</span>
  </blockquote>
  <svg class="review-tail" width="24" height="40" viewBox="0 0 24 40"><path d="M0 0h22v40z" fill="#1c9ce0"/></svg>

  <p class="web">www.<b>brightsparkelectrical</b>.com.au</p>
  <p class="fine-print">
    <span>*Mention this ad when booking to receive offer. Limit one per household</span>
    <span class="divider">*Cannot be combined with any other offer</span>
  </p>
</section>

</body>
</html>
```